Cybersecurity Start-Up - Korvelo

We need a power-point design for a new company based in Madrid (Spain) called 'Korvelo'. We aim to provide cybersecurity services to small- medium size companies for whom security is critical but paying big money to huge companies is not affordable.

The final design should communicate several things. As technology company which provides cybersecurity, it should be seen as something modern and futuristic , combined with safety and protection.

The company name Korvelo comes from Numantia, an ancient Celtiberian settlement in Spain which is famous for its role in the Celtiberian Wars (130 BC). They fought with Rome for 20 years , while being numerical inferior. And they won several times. When a final siege ocurred after a massive deployment of Rome legions, they held their ground for more than a year without food. When the situation was not longer sustainable, they decided to commit suicide rather than become slaves.

So the vision to hold the ground no matter what, should be communicated too
Updates

Need extra days to review

Requirements
Must have
• Check files attached for the logo of the company

```html
<!DOCTYPE html>
<html lang="en">
<head>
<meta charset="utf-8">
<title>Korvelo — Presentation Template</title>
<link href="https://fonts.googleapis.com/css2?family=Montserrat:wght@400;600;700;800&display=swap" rel="stylesheet">
<style>
:root{
  --orange:#f26522;
  --orange-soft:#f7a57a;
  --navy:#2c3b4b;
  --navy-deep:#1d2935;
  --grey:#eef0f2;
  --grey-mid:#c9ced4;
  --ink:#3a4450;
  --muted:#8a939c;
  --white:#ffffff;
  --page:#e4e6e9;
}
*{margin:0;padding:0;box-sizing:border-box}
html,body{width:702px;height:1200px;overflow:hidden;background:var(--page);font-family:"Montserrat",Arial,sans-serif;color:var(--ink)}
.deck{width:702px;height:1200px;padding:5px;display:grid;grid-template-columns:repeat(3,1fr);grid-template-rows:repeat(9,1fr);gap:5px}
.slide{position:relative;overflow:hidden;background:var(--white);box-shadow:0 1px 2px rgba(0,0,0,.15)}
.slide-head{position:absolute;left:8px;right:8px;top:5px;display:flex;justify-content:space-between;font-size:4.2px;font-weight:600;color:var(--ink)}
.slide-head b{color:var(--orange)}
.brand{font-weight:800;color:var(--navy);display:inline-flex;align-items:center;gap:2px}
.brand::before{content:"";width:4px;height:4px;background:var(--orange);border-radius:50%}
.slide-foot{position:absolute;left:0;right:0;bottom:0;height:2px;background:var(--orange)}
.photo{position:absolute;background:linear-gradient(135deg,#9aa3ad,#5d6873)}
.photo.warm{background:linear-gradient(135deg,#d8c4b2,#8a7566)}
.photo.dark{background:linear-gradient(135deg,#3b4a5a,#1b2530)}
.photo.light{background:linear-gradient(135deg,#e3e6ea,#b9c0c8)}
.h{font-weight:700;color:var(--navy);line-height:1.15}
.h-o{color:var(--orange)}
.p{font-size:3.6px;line-height:1.45;color:var(--muted)}
.abs{position:absolute}
.title-big{font-size:11px;font-weight:800;letter-spacing:.2px;color:var(--white)}
.sub{font-size:4.5px;color:var(--white);opacity:.85}
.logo-lg{font-size:9px;font-weight:800;color:var(--white);display:flex;align-items:center;gap:3px}
.logo-lg::before{content:"";width:6px;height:6px;background:var(--orange);border-radius:50%}
.bar-track{height:3px;background:var(--grey);margin-top:2px}
.bar-fill{height:3px;background:var(--orange)}
.bar-fill.navy{background:var(--navy)}
.icon-row{display:flex;align-items:flex-start;gap:4px;margin-bottom:6px}
.dot{width:8px;height:8px;border-radius:50%;background:var(--orange);flex:none}
.dot.navy{background:var(--navy)}
.mini-h{font-size:4.2px;font-weight:700;color:var(--navy)}
table{border-collapse:collapse;font-size:3.6px;width:100%}
th{background:var(--orange);color:var(--white);font-weight:600;padding:2.5px 3px;text-align:left}
td{padding:2.4px 3px;color:var(--muted);border-bottom:.5px solid var(--grey-mid)}
tr:nth-child(even) td{background:var(--grey)}
</style>
</head>
<body>
<main class="deck">

<!-- Row 1: title slides -->
<section class="slide" style="background:var(--orange)">
  <div class="photo warm" style="left:110px;top:0;right:0;bottom:0;background:linear-gradient(120deg,#f58a4f,#c9541c)" role="img" aria-label="Hand touching a glowing security shield"></div>
  <div class="abs logo-lg" style="left:10px;top:12px">Korvelo</div>
  <div class="abs title-big" style="left:10px;top:54px">POWERPOINT TITLE</div>
  <div class="abs sub" style="left:10px;top:70px">Your subtitle goes here</div>
  <div class="abs" style="left:0;right:0;bottom:0;height:14px;background:var(--white)"></div>
</section>

<section class="slide" style="background:var(--navy-deep)">
  <div class="photo dark" style="left:120px;top:0;right:0;bottom:0" role="img" aria-label="Digital security shield graphic"></div>
  <svg class="abs" style="left:150px;top:28px" width="52" height="60" viewBox="0 0 100 115"><path d="M50 3 L97 17 V55 C97 84 74 103 50 112 C26 103 3 84 3 55 V17 Z" fill="none" stroke="var(--orange)" stroke-width="6"/></svg>
  <div class="abs logo-lg" style="left:10px;top:12px">Korvelo</div>
  <div class="abs title-big" style="left:10px;top:54px;color:var(--orange)">POWERPOINT TITLE</div>
  <div class="abs sub" style="left:10px;top:70px">Your subtitle goes here</div>
  <div class="abs" style="left:0;right:0;bottom:0;height:10px;background:var(--orange)"></div>
</section>

<section class="slide">
  <div class="photo light" style="left:115px;top:0;right:0;height:80px" role="img" aria-label="Person working on a laptop in grey tones"></div>
  <div class="abs logo-lg" style="left:10px;top:12px;color:var(--navy)">Korvelo</div>
  <div class="abs" style="left:0;top:46px;width:125px;height:26px;background:var(--orange)"></div>
  <div class="abs title-big" style="left:10px;top:50px">POWERPOINT TITLE</div>
  <div class="abs sub" style="left:10px;top:63px">Your subtitle goes here</div>
  <div class="photo" style="left:0;right:0;bottom:0;height:36px;background:linear-gradient(90deg,#7c8792,#4a5560)" role="img" aria-label="Office team at work"></div>
</section>

<!-- Row 2 -->
<section class="slide">
  <div class="slide-head"><span>Korvelo <b>Powerpoint Template</b></span><span class="brand">Korvelo</span></div>
  <svg class="abs" style="left:14px;top:20px" width="80" height="94" viewBox="0 0 100 115" role="img" aria-label="Business person portrait in shield frame"><defs><linearGradient id="gp1" x1="0" y1="0" x2="1" y2="1"><stop offset="0" stop-color="#9aa3ad"/><stop offset="1" stop-color="#5d6873"/></linearGradient></defs><path d="M50 3 L97 17 V55 C97 84 74 103 50 112 C26 103 3 84 3 55 V17 Z" fill="url(#gp1)" stroke="var(--orange)" stroke-width="5"/></svg>
  <div class="abs h" style="left:110px;top:28px;width:105px;font-size:7px">Write Something About <span class="h-o">Your Title or Topic Here</span></div>
  <p class="abs p" style="left:110px;top:52px;width:108px">Add a short summary of the topic here. Keep lines brief so the key message stays clear and easy to read for the audience.</p>
  <p class="abs p" style="left:110px;top:78px;width:108px">Add a second short paragraph with supporting detail about the service.</p>
  <div class="slide-foot"></div>
</section>

<section class="slide">
  <div class="slide-head"><span>Korvelo <b>Powerpoint Template</b></span><span class="brand">Korvelo</span></div>
  <div class="photo" style="left:0;right:0;top:14px;height:52px" role="img" aria-label="Hands typing on a laptop keyboard"></div>
  <div class="abs" style="left:0;top:14px;width:84px;height:52px;background:var(--orange)"></div>
  <div class="abs h" style="left:8px;top:24px;width:72px;font-size:6.5px;color:var(--white)">Write Something About Your Title or Topic Here</div>
  <p class="abs p" style="left:10px;top:76px;width:100px">Add a short summary of the topic here with brief supporting lines.</p>
  <p class="abs p" style="left:118px;top:76px;width:100px">Add a second short note that explains the main benefit.</p>
  <div class="slide-foot"></div>
</section>

<section class="slide">
  <div class="slide-head"><span>Korvelo <b>Powerpoint Template</b></span><span class="brand">Korvelo</span></div>
  <div class="abs h" style="left:10px;top:24px;width:100px;font-size:7px">Write Something About <span class="h-o">Your Title or Topic Here</span></div>
  <p class="abs p" style="left:10px;top:50px;width:105px">Add a short summary of the topic here. Keep lines brief so the message stays clear.</p>
  <div class="photo" style="left:125px;top:18px;width:94px;height:58px" role="img" aria-label="Person working at a desk"></div>
  <p class="abs p" style="left:125px;top:82px;width:94px">Add a caption for the image with a short line of detail.</p>
  <div class="slide-foot"></div>
</section>

<!-- Row 3 -->
<section class="slide">
  <div class="slide-head"><span>Korvelo <b>Powerpoint Template</b></span><span class="brand">Korvelo</span></div>
  <svg class="abs" style="left:22px;top:26px" width="28" height="32" viewBox="0 0 100 115"><path d="M50 3 L97 17 V55 C97 84 74 103 50 112 C26 103 3 84 3 55 V17 Z" fill="var(--orange)"/><path d="M32 58 L46 72 L70 44" fill="none" stroke="#fff" stroke-width="8"/></svg>
  <svg class="abs" style="left:100px;top:26px" width="28" height="32" viewBox="0 0 100 115"><path d="M50 3 L97 17 V55 C97 84 74 103 50 112 C26 103 3 84 3 55 V17 Z" fill="var(--orange)"/><circle cx="50" cy="55" r="16" fill="none" stroke="#fff" stroke-width="7"/></svg>
  <svg class="abs" style="left:178px;top:26px" width="28" height="32" viewBox="0 0 100 115"><path d="M50 3 L97 17 V55 C97 84 74 103 50 112 C26 103 3 84 3 55 V17 Z" fill="var(--navy)"/><rect x="36" y="48" width="28" height="24" fill="#fff"/><path d="M40 48 V40 a10 10 0 0 1 20 0 V48" fill="none" stroke="#fff" stroke-width="6"/></svg>
  <div class="abs mini-h" style="left:12px;top:66px;width:50px;text-align:center">Insert Title</div>
  <div class="abs mini-h" style="left:90px;top:66px;width:50px;text-align:center">Insert Title</div>
  <div class="abs mini-h" style="left:168px;top:66px;width:50px;text-align:center">Insert Title</div>
  <p class="abs p" style="left:10px;top:74px;width:56px;text-align:center">Add short text here to describe this point.</p>
  <p class="abs p" style="left:88px;top:74px;width:56px;text-align:center">Add short text here to describe this point.</p>
  <p class="abs p" style="left:166px;top:74px;width:56px;text-align:center">Add short text here to describe this point.</p>
  <div class="slide-foot"></div>
</section>

<section class="slide">
  <div class="slide-head"><span>Korvelo <b>Powerpoint Template</b></span><span class="brand">Korvelo</span></div>
  <div class="abs" style="left:14px;top:22px;width:95px">
    <div class="icon-row"><span class="dot"></span><div><div class="mini-h">Insert Title</div><p class="p">Add short supporting text here.</p></div></div>
    <div class="icon-row"><span class="dot"></span><div><div class="mini-h">Insert Title</div><p class="p">Add short supporting text here.</p></div></div>
    <div class="icon-row"><span class="dot navy"></span><div><div class="mini-h">Insert Title</div><p class="p">Add short supporting text here.</p></div></div>
  </div>
  <div class="abs" style="left:120px;top:22px;width:95px">
    <div class="icon-row"><span class="dot"></span><div><div class="mini-h">Insert Title</div><p class="p">Add short supporting text here.</p></div></div>
    <div class="icon-row"><span class="dot"></span><div><div class="mini-h">Insert Title</div><p class="p">Add short supporting text here.</p></div></div>
    <div class="icon-row"><span class="dot navy"></span><div><div class="mini-h">Insert Title</div><p class="p">Add short supporting text here.</p></div></div>
  </div>
  <div class="slide-foot"></div>
</section>

<section class="slide">
  <div class="slide-head"><span>Korvelo <b>Powerpoint Template</b></span><span class="brand">Korvelo</span></div>
  <svg class="abs" style="left:10px;top:48px" width="209" height="20" viewBox="0 0 209 20">
    <polygon points="0,0 48,0 56,10 48,20 0,20" fill="var(--orange)"/>
    <polygon points="52,0 100,0 108,10 100,20 52,20 60,10" fill="var(--navy)"/>
    <polygon points="104,0 152,0 160,10 152,20 104,20 112,10" fill="var(--orange)"/>
    <polygon points="156,0 201,0 209,10 201,20 156,20 164,10" fill="var(--navy)"/>
  </svg>
  <div class="abs" style="left:22px;top:28px;width:14px;height:14px;border:1.5px solid var(--orange);border-radius:50%"></div>
  <div class="abs" style="left:76px;top:28px;width:14px;height:14px;border:1.5px solid var(--navy);border-radius:50%"></div>
  <div class="abs" style="left:128px;top:28px;width:14px;height:14px;border:1.5px solid var(--orange);border-radius:50%"></div>
  <div class="abs" style="left:180px;top:28px;width:14px;height:14px;border:1.5px solid var(--navy);border-radius:50%"></div>
  <p class="abs p" style="left:10px;top:76px;width:46px">Add a brief step note here.</p>
  <p class="abs p" style="left:63px;top:76px;width:46px">Add a brief step note here.</p>
  <p class="abs p" style="left:115px;top:76px;width:46px">Add a brief step note here.</p>
  <p class="abs p" style="left:167px;top:76px;width:46px">Add a brief step note here.</p>
  <div class="slide-foot"></div>
</section>

<!-- Row 4 -->
<section class="slide">
  <div class="slide-head"><span>Korvelo <b>Powerpoint Template</b></span><span class="brand">Korvelo</span></div>
  <svg class="abs" style="left:14px;top:24px" width="200" height="46" viewBox="0 0 200 46">
    <g fill="none" stroke-width="7">
      <circle cx="30" cy="23" r="18" stroke="var(--grey)"/><circle cx="30" cy="23" r="18" stroke="var(--orange)" stroke-dasharray="85 113" transform="rotate(-90 30 23)"/>
      <circle cx="100" cy="23" r="18" stroke="var(--grey)"/><circle cx="100" cy="23" r="18" stroke="var(--orange)" stroke-dasharray="62 113" transform="rotate(-90 100 23)"/>
      <circle cx="170" cy="23" r="18" stroke="var(--grey)"/><circle cx="170" cy="23" r="18" stroke="var(--navy)" stroke-dasharray="96 113" transform="rotate(-90 170 23)"/>
    </g>
    <g font-size="6" font-weight="700" text-anchor="middle" fill="var(--navy)" font-family="Montserrat, sans-serif"><text x="30" y="25">75%</text><text x="100" y="25">55%</text><text x="170" y="25">85%</text></g>
  </svg>
  <div class="abs mini-h" style="left:24px;top:78px;width:40px;text-align:center">Your Title</div>
  <div class="abs mini-h" style="left:94px;top:78px;width:40px;text-align:center">Your Title</div>
  <div class="abs mini-h" style="left:164px;top:78px;width:40px;text-align:center">Your Title</div>
  <p class="abs p" style="left:18px;top:86px;width:52px;text-align:center">Add short text about this value.</p>
  <p class="abs p" style="left:88px;top:86px;width:52px;text-align:center">Add short text about this value.</p>
  <p class="abs p" style="left:158px;top:86px;width:52px;text-align:center">Add short text about this value.</p>
  <div class="slide-foot"></div>
</section>

<section class="slide">
  <div class="slide-head"><span>Korvelo <b>Powerpoint Template</b></span><span class="brand">Korvelo</span></div>
  <div class="abs h" style="left:10px;top:24px;width:90px;font-size:6.5px">Write Something About <span class="h-o">Your Title or Topic Here</span></div>
  <p class="abs p" style="left:10px;top:48px;width:92px">Add a short summary of the chart here and explain the main trend shown.</p>
  <svg class="abs" style="left:112px;top:22px" width="108" height="84" viewBox="0 0 108 84">
    <line x1="0" y1="82" x2="108" y2="82" stroke="var(--grey-mid)" stroke-width=".8"/>
    <rect x="6" y="40" width="8" height="42" fill="var(--orange)"/><rect x="15" y="56" width="8" height="26" fill="var(--navy)"/>
    <rect x="34" y="20" width="8" height="62" fill="var(--orange)"/><rect x="43" y="48" width="8" height="34" fill="var(--navy)"/>
    <rect x="62" y="30" width="8" height="52" fill="var(--orange)"/><rect x="71" y="10" width="8" height="72" fill="var(--navy)"/>
    <rect x="90" y="44" width="8" height="38" fill="var(--orange)"/><rect x="99" y="60" width="8" height="22" fill="var(--navy)"/>
  </svg>
  <div class="slide-foot"></div>
</section>

<section class="slide">
  <div class="abs h" style="left:0;right:0;top:8px;text-align:center;font-size:6px">Company <span class="h-o">Timeline</span></div>
  <div class="abs" style="left:114px;top:20px;width:1px;bottom:6px;background:var(--grey-mid)"></div>
  <div class="abs dot" style="left:111px;top:28px;width:7px;height:7px"></div>
  <div class="abs dot navy" style="left:111px;top:58px;width:7px;height:7px"></div>
  <div class="abs dot" style="left:111px;top:88px;width:7px;height:7px"></div>
  <div class="abs" style="left:20px;top:26px;width:84px;text-align:right"><div class="mini-h">2016</div><p class="p">Add a short milestone note here.</p></div>
  <div class="abs" style="left:126px;top:56px;width:84px"><div class="mini-h">2017</div><p class="p">Add a short milestone note here.</p></div>
  <div class="abs" style="left:20px;top:86px;width:84px;text-align:right"><div class="mini-h">2018</div><p class="p">Add a short milestone note here.</p></div>
</section>

<!-- Row 5 -->
<section class="slide">
  <div class="slide-head"><span>Korvelo <b>Powerpoint Template</b></span><span class="brand">Korvelo</span></div>
  <svg class="abs" style="left:12px;top:20px" width="100" height="94" viewBox="0 0 100 94">
    <g>
      <rect x="4" y="0" width="14" height="92" fill="var(--grey)"/><rect x="4" y="30" width="14" height="62" fill="var(--orange)"/>
      <rect x="30" y="0" width="14" height="92" fill="var(--grey)"/><rect x="30" y="14" width="14" height="78" fill="var(--orange)"/>
      <rect x="56" y="0" width="14" height="92" fill="var(--grey)"/><rect x="56" y="40" width="14" height="52" fill="var(--orange)"/>
      <rect x="82" y="0" width="14" height="92" fill="var(--grey)"/><rect x="82" y="22" width="14" height="70" fill="var(--navy)"/>
    </g>
  </svg>
  <div class="abs" style="left:126px;top:28px;width:92px">
    <div class="icon-row"><span class="dot"></span><div><div class="mini-h">Insert Title</div><p class="p">Add short supporting text here.</p></div></div>
    <div class="icon-row"><span class="dot"></span><div><div class="mini-h">Insert Title</div><p class="p">Add short supporting text here.</p></div></div>
    <div class="icon-row"><span class="dot navy"></span><div><div class="mini-h">Insert Title</div><p class="p">Add short supporting text here.</p></div></div>
  </div>
  <div class="slide-foot"></div>
</section>

<section class="slide">
  <div class="slide-head"><span>Korvelo <b>Powerpoint Template</b></span><span class="brand">Korvelo</span></div>
  <div class="abs" style="left:12px;right:12px;top:22px">
    <table>
      <thead><tr><th>Service</th><th>Plan A</th><th>Plan B</th><th>Plan C</th><th>Plan D</th></tr></thead>
      <tbody>
        <tr><td>Item One</td><td>Yes</td><td>Yes</td><td>No</td><td>Yes</td></tr>
        <tr><td>Item Two</td><td>No</td><td>Yes</td><td>Yes</td><td>Yes</td></tr>
        <tr><td>Item Three</td><td>Yes</td><td>No</td><td>Yes</td><td>No</td></tr>
        <tr><td>Item Four</td><td>Yes</td><td>Yes</td><td>Yes</td><td>Yes</td></tr>
        <tr><td>Item Five</td><td>No</td><td>No</td><td>Yes</td><td>Yes</td></tr>
      </tbody>
    </table>
  </div>
  <div class="slide-foot"></div>
</section>

<section class="slide">
  <div class="abs" style="left:114px;top:0;width:1px;bottom:6px;background:var(--grey-mid)"></div>
  <div class="abs dot navy" style="left:111px;top:14px;width:7px;height:7px"></div>
  <div class="abs dot" style="left:111px;top:46px;width:7px;height:7px"></div>
  <div class="abs dot navy" style="left:111px;top:78px;width:7px;height:7px"></div>
  <div class="abs" style="left:126px;top:12px;width:84px"><div class="mini-h">2019</div><p class="p">Add a short milestone note here.</p></div>
  <div class="abs" style="left:20px;top:44px;width:84px;text-align:right"><div class="mini-h">2020</div><p class="p">Add a short milestone note here.</p></div>
  <div class="abs" style="left:126px;top:76px;width:84px"><div class="mini-h">2021</div><p class="p">Add a short milestone note here.</p></div>
</section>

<!-- Row 6 -->
<section class="slide">
  <div class="slide-head"><span>Korvelo <b>Powerpoint Template</b></span><span class="brand">Korvelo</span></div>
  <svg class="abs" style="left:22px;top:22px" width="34" height="40" viewBox="0 0 100 115" role="img" aria-label="Team member portrait"><path d="M50 3 L97 17 V55 C97 84 74 103 50 112 C26 103 3 84 3 55 V17 Z" fill="#7b8590" stroke="var(--orange)" stroke-width="6"/></svg>
  <svg class="abs" style="left:98px;top:22px" width="34" height="40" viewBox="0 0 100 115" role="img" aria-label="Team member portrait"><path d="M50 3 L97 17 V55 C97 84 74 103 50 112 C26 103 3 84 3 55 V17 Z" fill="#7b8590" stroke="var(--orange)" stroke-width="6"/></svg>
  <svg class="abs" style="left:174px;top:22px" width="34" height="40" viewBox="0 0 100 115" role="img" aria-label="Team member portrait"><path d="M50 3 L97 17 V55 C97 84 74 103 50 112 C26 103 3 84 3 55 V17 Z" fill="#7b8590" stroke="var(--navy)" stroke-width="6"/></svg>
  <div class="abs mini-h" style="left:14px;top:68px;width:50px;text-align:center">Name Here</div>
  <div class="abs mini-h" style="left:90px;top:68px;width:50px;text-align:center">Name Here</div>
  <div class="abs mini-h" style="left:166px;top:68px;width:50px;text-align:center">Name Here</div>
  <p class="abs p" style="left:12px;top:76px;width:54px;text-align:center">Job title and a short note.</p>
  <p class="abs p" style="left:88px;top:76px;width:54px;text-align:center">Job title and a short note.</p>
  <p class="abs p" style="left:164px;top:76px;width:54px;text-align:center">Job title and a short note.</p>
  <div class="slide-foot"></div>
</section>

<section class="slide">
  <div class="slide-head"><span>Korvelo <b>Powerpoint Template</b></span><span class="brand">Korvelo</span></div>
  <div class="abs dot" style="left:12px;top:26px;width:10px;height:10px"></div>
  <div class="abs h" style="left:26px;top:26px;font-size:8px">John Doe</div>
  <p class="abs p" style="left:12px;top:42px;width:100px">Add a short profile of the team member, their role and their experience in security.</p>
  <p class="abs p" style="left:12px;top:66px;width:100px">Add a second short line with more detail.</p>
  <svg class="abs" style="left:132px;top:18px" width="80" height="94" viewBox="0 0 100 115" role="img" aria-label="Portrait of John Doe in shield frame"><path d="M50 3 L97 17 V55 C97 84 74 103 50 112 C26 103 3 84 3 55 V17 Z" fill="#6f7a85" stroke="var(--orange)" stroke-width="5"/></svg>
  <div class="slide-foot"></div>
</section>

<section class="slide">
  <div class="photo light" style="inset:0" role="img" aria-label="Faded city and office backdrop"></div>
  <div class="slide-head"><span>Korvelo <b>Powerpoint Template</b></span><span class="brand">Korvelo</span></div>
  <div class="abs h" style="left:0;right:0;top:50px;text-align:center;font-size:7px">Write Something About Your Title</div>
  <p class="abs p" style="left:50px;right:50px;top:64px;text-align:center;color:var(--ink)">Add a short statement for this section here.</p>
</section>

<!-- Row 7 -->
<section class="slide">
  <div class="slide-head"><span>Korvelo <b>Powerpoint Template</b></span><span class="brand">Korvelo</span></div>
  <div class="photo warm" style="left:0;top:14px;width:100px;bottom:0" role="img" aria-label="Businessman in an office"></div>
  <div class="abs h" style="left:110px;top:22px;width:108px;font-size:6.5px">Write Something About <span class="h-o">Your Title or Topic Here</span></div>
  <div class="abs" style="left:110px;top:48px;width:108px">
    <div class="mini-h">Skill One</div><div class="bar-track"><div class="bar-fill" style="width:80%"></div></div>
    <div class="mini-h" style="margin-top:5px">Skill Two</div><div class="bar-track"><div class="bar-fill navy" style="width:65%"></div></div>
    <div class="mini-h" style="margin-top:5px">Skill Three</div><div class="bar-track"><div class="bar-fill" style="width:90%"></div></div>
  </div>
  <div class="slide-foot"></div>
</section>

<section class="slide">
  <div class="slide-head"><span>Korvelo <b>Powerpoint Template</b></span><span class="brand">Korvelo</span></div>
  <div class="abs" style="left:12px;top:30px;width:98px;height:66px;background:var(--navy)"></div>
  <div class="abs" style="left:119px;top:30px;width:98px;height:66px;background:var(--navy)"></div>
  <div class="abs dot" style="left:56px;top:38px"></div>
  <div class="abs dot" style="left:163px;top:38px"></div>
  <div class="abs mini-h" style="left:12px;top:52px;width:98px;text-align:center;color:var(--white)">Insert Title</div>
  <div class="abs mini-h" style="left:119px;top:52px;width:98px;text-align:center;color:var(--white)">Insert Title</div>
  <p class="abs p" style="left:20px;top:60px;width:82px;text-align:center;color:var(--grey-mid)">Add short supporting text about this item here.</p>
  <p class="abs p" style="left:127px;top:60px;width:82px;text-align:center;color:var(--grey-mid)">Add short supporting text about this item here.</p>
  <div class="slide-foot"></div>
</section>

<section class="slide">
  <div class="photo warm" style="left:0;right:0;top:0;height:58px" role="img" aria-label="Hands working on documents and a tablet"></div>
  <div class="abs" style="left:14px;top:46px;width:24px;height:24px;background:var(--orange)"></div>
  <svg class="abs" style="left:19px;top:51px" width="14" height="14" viewBox="0 0 20 20"><circle cx="10" cy="10" r="6" fill="none" stroke="#fff" stroke-width="3" stroke-dasharray="3 1.8"/><circle cx="10" cy="10" r="2.5" fill="#fff"/></svg>
  <div class="abs h" style="left:46px;top:64px;font-size:6px">Insert Title Here</div>
  <p class="abs p" style="left:14px;top:78px;width:96px">Add a short summary of the topic here with supporting detail.</p>
  <p class="abs p" style="left:120px;top:78px;width:96px">Add a second short note that explains the main benefit.</p>
  <div class="slide-foot"></div>
</section>

<!-- Row 8 -->
<section class="slide">
  <div class="abs" style="left:0;top:0;width:96px;bottom:0;background:var(--navy)"></div>
  <div class="abs h" style="left:10px;top:14px;font-size:6px;color:var(--white)">Insert Text Here</div>
  <div class="photo" style="left:20px;top:38px;width:58px;height:76px;border:3px solid var(--navy-deep);border-radius:4px" role="img" aria-label="Tablet showing a slide"></div>
  <div class="abs h" style="left:108px;top:18px;width:108px;font-size:6.5px">Write Something About <span class="h-o">Your Title Here</span></div>
  <p class="abs p" style="left:108px;top:40px;width:108px">Add a short summary of the product here with key details and benefits for the client.</p>
  <p class="abs p" style="left:108px;top:66px;width:108px">Add a second short paragraph with more detail.</p>
  <div class="slide-foot"></div>
</section>

<section class="slide">
  <div class="slide-head"><span>Korvelo <b>Powerpoint Template</b></span><span class="brand">Korvelo</span></div>
  <div class="abs h" style="left:10px;top:20px;font-size:6.5px">Insert Text Here</div>
  <div class="abs" style="left:10px;top:34px;width:92px">
    <div class="icon-row"><span class="dot"></span><p class="p">Add short supporting text here.</p></div>
    <div class="icon-row"><span class="dot"></span><p class="p">Add short supporting text here.</p></div>
    <div class="icon-row"><span class="dot navy"></span><p class="p">Add short supporting text here.</p></div>
  </div>
  <div class="photo" style="left:112px;top:24px;width:104px;height:64px;border:3px solid var(--navy-deep)" role="img" aria-label="Desktop monitor showing the brand screen"></div>
  <div class="abs" style="left:156px;top:88px;width:16px;height:10px;background:var(--grey-mid)"></div>
  <div class="abs" style="left:146px;top:98px;width:36px;height:2px;background:var(--grey-mid)"></div>
  <div class="slide-foot"></div>
</section>

<section class="slide">
  <div class="abs" style="left:0;top:0;width:110px;bottom:0;background:var(--orange)"></div>
  <div class="abs h" style="left:10px;top:16px;font-size:6.5px;color:var(--white)">Insert Text Here</div>
  <p class="abs p" style="left:10px;top:30px;width:62px;color:var(--white)">Add a short summary of the app here.</p>
  <div class="photo" style="left:78px;top:24px;width:40px;height:80px;border:3px solid var(--navy-deep);border-radius:5px" role="img" aria-label="Smartphone showing an app screen"></div>
  <div class="abs" style="left:130px;top:22px;width:88px">
    <div class="icon-row"><span class="dot"></span><div><div class="mini-h">Insert Title</div><p class="p">Add short text here.</p></div></div>
    <div class="icon-row"><span class="dot"></span><div><div class="mini-h">Insert Title</div><p class="p">Add short text here.</p></div></div>
    <div class="icon-row"><span class="dot navy"></span><div><div class="mini-h">Insert Title</div><p class="p">Add short text here.</p></div></div>
  </div>
</section>

<!-- Row 9 -->
<section class="slide" style="background:var(--navy-deep)">
  <div class="photo dark" style="inset:0" role="img" aria-label="Dark technology backdrop"></div>
  <svg class="abs" style="left:14px;top:66px" width="30" height="34" viewBox="0 0 100 115"><path d="M50 3 L97 17 V55 C97 84 74 103 50 112 C26 103 3 84 3 55 V17 Z" fill="var(--orange)"/><path d="M32 58 L46 72 L70 44" fill="none" stroke="#fff" stroke-width="8"/></svg>
  <div class="abs title-big" style="left:52px;top:74px">SECTION BREAK</div>
  <div class="abs sub" style="left:52px;top:88px">Your subtitle goes here</div>
</section>

<section class="slide">
  <div class="abs brand" style="left:0;right:0;top:16px;justify-content:center;font-size:8px">Korvelo</div>
  <div class="abs h" style="left:0;right:0;top:38px;text-align:center;font-size:10px">CONTACT US</div>
  <p class="abs p" style="left:40px;right:40px;top:54px;text-align:center">Add a short closing line for the audience here.</p>
  <div class="abs" style="left:20px;right:20px;top:74px;display:flex;justify-content:space-between">
    <div style="width:40px;text-align:center"><span class="dot" style="display:block;margin:0 auto 3px;width:12px;height:12px"></span><p class="p">Calle Mayor 10</p></div>
    <div style="width:40px;text-align:center"><span class="dot navy" style="display:block;margin:0 auto 3px;width:12px;height:12px"></span><p class="p">+34 900 000 000</p></div>
    <div style="width:40px;text-align:center"><span class="dot" style="display:block;margin:0 auto 3px;width:12px;height:12px"></span><p class="p">hola@korvelo.es</p></div>
    <div style="width:40px;text-align:center"><span class="dot navy" style="display:block;margin:0 auto 3px;width:12px;height:12px"></span><p class="p">korvelo.es</p></div>
  </div>
  <div class="slide-foot"></div>
</section>

<section class="slide">
  <div class="photo dark" style="left:0;right:0;top:0;height:60px" role="img" aria-label="Dark city skyline"></div>
  <div class="abs logo-lg" style="left:0;right:0;top:12px;justify-content:center">Korvelo</div>
  <div class="abs title-big" style="left:0;right:0;top:32px;text-align:center">CONTACT US</div>
  <div class="abs" style="left:20px;right:20px;top:74px;display:flex;justify-content:space-between">
    <div style="width:40px;text-align:center"><span class="dot navy" style="display:block;margin:0 auto 3px;width:12px;height:12px"></span><p class="p">Calle Mayor 10</p></div>
    <div style="width:40px;text-align:center"><span class="dot" style="display:block;margin:0 auto 3px;width:12px;height:12px"></span><p class="p">+34 900 000 000</p></div>
    <div style="width:40px;text-align:center"><span class="dot navy" style="display:block;margin:0 auto 3px;width:12px;height:12px"></span><p class="p">hola@korvelo.es</p></div>
    <div style="width:40px;text-align:center"><span class="dot" style="display:block;margin:0 auto 3px;width:12px;height:12px"></span><p class="p">korvelo.es</p></div>
  </div>
  <div class="slide-foot"></div>
</section>

</main>
</body>
</html>
```